Real Estate Business Card

Our Company, Brindle Real Estate needs a business card design. It will need a spot for our Name, Office Number, Cell number, email, website address. Brindlerealestate.example and Address. Please utilize our logo for the aesthetic feel of the card. We would like something that is noticeable but looks professional.

Please include our company tagline. "Where Every Move Feels Like Coming Home"

Industry/Entity Type

Business

Requirements
Should not have
• Black colored Font is OK. But other than that no black

```html
<!DOCTYPE html>
<html lang="en">
<head>
<meta charset="utf-8">
<title>Brindle Real Estate – Business Card</title>
<link href="https://fonts.googleapis.com/css2?family=Source+Sans+3:wght@400;600;700&display=swap" rel="stylesheet">
<style>
  :root {
    --orange: #e8711f;
    --navy: #2e3a8c;
    --paper: #fbfbfa;
    --stage: #e6e6e9;
    --white: #ffffff;
  }
  * { box-sizing: border-box; margin: 0; padding: 0; }
  html, body {
    width: 1200px; height: 723px; overflow: hidden;
    background: var(--stage);
    font-family: "Source Sans 3", Arial, sans-serif;
  }
  .canvas {
    position: relative; width: 1200px; height: 723px;
    display: flex; align-items: center; justify-content: center; gap: 60px;
  }
  .card {
    position: relative; width: 520px; height: 298px;
    border-radius: 4px;
    box-shadow: 0 6px 18px rgba(60, 60, 80, 0.18);
    overflow: hidden;
  }
  /* Front side */
  .card--front {
    background: var(--orange);
    display: flex; flex-direction: column; justify-content: center; align-items: center;
    color: var(--white);
  }
  .brand { display: flex; align-items: center; gap: 12px; }
  .brand__square { width: 34px; height: 34px; background: var(--white); border-radius: 4px; }
  .brand__name { font-size: 38px; font-weight: 600; letter-spacing: 0.2px; line-height: 1; }
  .tagline { margin-top: 8px; font-size: 13.5px; font-weight: 700; letter-spacing: 0.2px; padding-left: 46px; }
  /* Back side */
  .card--back { background: var(--paper); }
  .back__brand {
    position: absolute; left: 40px; top: 146px;
    display: flex; align-items: center; gap: 10px;
  }
  .back__square { width: 30px; height: 30px; background: var(--navy); border-radius: 4px; flex: none; }
  .back__name { color: var(--navy); font-size: 19px; font-weight: 600; line-height: 1.05; }
  .contact { position: absolute; left: 246px; top: 48px; }
  .contact__name { color: var(--navy); font-weight: 700; font-size: 14px; letter-spacing: 0.3px; }
  .contact__title { color: var(--orange); font-size: 11px; font-weight: 600; margin-top: 1px; }
  .contact__lines { margin-top: 16px; padding-left: 24px; font-size: 11px; line-height: 1.35; color: var(--orange); }
  .contact__lines b { color: var(--navy); font-weight: 700; }
  .office { margin-top: 14px; padding-left: 24px; color: var(--navy); font-size: 11px; line-height: 1.25; }
  .office__company { font-weight: 700; }
  .office__zip { padding-left: 58px; }
  .website { margin-top: 16px; padding-left: 52px; color: var(--orange); font-weight: 700; font-size: 11.5px; }
</style>
</head>
<body>
<main class="canvas">
  <section class="card card--front" aria-label="Card front">
    <div class="brand">
      <span class="brand__square"></span>
      <span class="brand__name">Brindle Real Estate</span>
    </div>
    <p class="tagline">Where Every Move Feels Like Coming Home</p>
  </section>

  <section class="card card--back" aria-label="Card back">
    <div class="back__brand">
      <span class="back__square"></span>
      <span class="back__name">Brindle<br>Real Estate</span>
    </div>
    <div class="contact">
      <p class="contact__name">YOUR NAME</p>
      <p class="contact__title">Title</p>
      <p class="contact__lines">
        <b>T:</b> 123 56 789<br>
        <b>M:</b> 123 456 0987<br>
        <b>E:</b> yourname@brindlerealestate.example
      </p>
      <div class="office">
        <p class="office__company">Brindle Real Estate</p>
        <p>City name, Country,</p>
        <p class="office__zip">NY 1234</p>
      </div>
      <p class="website">www.brindlerealestate.example</p>
    </div>
  </section>
</main>
</body>
</html>
```